Original business card of a small accounting firm

My firm specializes in accounting and taxes for small businesses. I'm looking for an original and creative business card as a marketing tool to give to prospective clients; however since we are a professional firm the card must also appear professional. I'm uploading a few examples of what I believe may fit my needs. Please feel free to use them as a jumping off point. Lastly, I'm uploading the company logo which I'd like to be the focal point on the back of the card and somewhat incorporated on the front on a smaller scale. I hope my description was helpful.
Target Market(s)
Tax clients and small businesses
Industry/Entity Type
Accounting
Contact Information for Business Card
Gerald Whitcombe
Certified Public Accountant │President
Whitcombe Advisors
T│ (555) 417-2863
Email│GWhitcombe@WhitcombeAdvisors.example
Look and feel
Each slider illustrates characteristics of the customer's brand and the style your logo design should communicate.

```html
<!DOCTYPE html>
<html lang="en">
<head>
<meta charset="utf-8">
<title>Whitcombe Advisors – Business Card</title>
<link rel="stylesheet" href="https://fonts.googleapis.com/css2?family=Exo+2:wght@400;500;600&display=swap">
<style>
  :root {
    --page-bg: #e9eaec;
    --card-light: #ffffff;
    --card-shade: #e4e5e8;
    --brand-blue: #2f5fc4;
    --brand-blue-deep: #2444a8;
    --brand-blue-light: #3f8be0;
    --accent-cyan: #1fa3e8;
    --rule-grey: #6c6f75;
    --text-dark: #3a3d42;
    --text-body: #2b2d31;
  }
  * { margin: 0; padding: 0; box-sizing: border-box; }
  html, body {
    width: 1200px; height: 900px; overflow: hidden;
    background: var(--page-bg);
    font-family: "Exo 2", Arial, sans-serif;
  }
  .canvas {
    width: 1200px; height: 900px;
    display: flex; align-items: center; justify-content: center;
  }
  .business-card {
    position: relative;
    width: 1000px; height: 580px;
    border-radius: 56px;
    overflow: hidden;
    background: radial-gradient(ellipse at 60% 30%, var(--card-light) 0%, var(--card-light) 40%, var(--card-shade) 100%);
    box-shadow: 0 18px 40px rgba(0,0,0,0.18);
  }
  .swoosh { position: absolute; inset: 0; width: 100%; height: 100%; }
  .brand-lockup {
    position: absolute; left: 80px; top: 95px;
    display: flex; flex-direction: column; gap: 8px;
  }
  .brand-name {
    display: flex; align-items: center; gap: 14px;
    font-size: 48px; font-weight: 600; color: var(--text-dark);
    letter-spacing: 0.5px; line-height: 1.1;
  }
  .brand-square {
    width: 32px; height: 32px; background: var(--brand-blue);
  }
  .brand-tagline {
    font-size: 16px; font-weight: 400; color: var(--text-dark);
    text-transform: uppercase; letter-spacing: 3px;
    padding-left: 46px;
  }
  .contact-column {
    position: absolute; right: 70px; top: 60px;
    text-align: right; color: var(--text-body);
  }
  .person-name {
    font-size: 27px; font-weight: 500; color: var(--accent-cyan);
    letter-spacing: 1.5px; text-transform: uppercase; line-height: 1.3;
  }
  .person-title { font-size: 20px; margin-top: 2px; }
  .office-address { font-size: 19px; line-height: 1.4; margin-top: 30px; font-style: normal; }
  .contact-list { list-style: none; margin-top: 34px; }
  .contact-item {
    display: flex; justify-content: flex-end; align-items: center; gap: 12px;
    font-size: 18px; letter-spacing: 0.6px; height: 32px;
  }
  .contact-item svg { width: 20px; height: 20px; fill: var(--accent-cyan); flex: none; }
  .contact-item.gap-above { margin-top: 6px; }
</style>
</head>
<body>
<main class="canvas">
  <article class="business-card">
    <svg class="swoosh" viewBox="0 0 1000 580" preserveAspectRatio="none" aria-hidden="true">
      <defs>
        <linearGradient id="blueSweep" x1="0" y1="0" x2="1" y2="1">
          <stop offset="0" stop-color="var(--brand-blue-deep)"/>
          <stop offset="0.55" stop-color="var(--brand-blue-light)"/>
          <stop offset="1" stop-color="var(--brand-blue)"/>
        </linearGradient>
      </defs>
      <path d="M0,232 C250,372 600,492 1000,508 L1000,520 C600,508 255,388 0,258 Z" fill="var(--brand-blue)"/>
      <path d="M0,265 C258,395 610,512 1000,526 L1000,534 C610,522 262,405 0,279 Z" fill="var(--rule-grey)"/>
      <path d="M0,287 C265,410 615,528 1000,540 L1000,580 L0,580 Z" fill="url(#blueSweep)"/>
    </svg>

    <header class="brand-lockup">
      <div class="brand-name"><span class="brand-square"></span>Whitcombe Advisors</div>
      <div class="brand-tagline">Small Business Accounting and Taxes</div>
    </header>

    <section class="contact-column">
      <h1 class="person-name">Martin Hale</h1>
      <p class="person-title">Managing Director</p>
      <address class="office-address">210, 4th floor, Elm Court<br>Road NWK</address>
      <ul class="contact-list">
        <li class="contact-item">(555) 301-4472
          <svg viewBox="0 0 24 24"><path d="M6.6 10.8a15 15 0 0 0 6.6 6.6l2.2-2.2c.3-.3.7-.4 1-.2 1.1.4 2.3.6 3.6.6.6 0 1 .4 1 1V20c0 .6-.4 1-1 1A17 17 0 0 1 3 4c0-.6.4-1 1-1h3.5c.6 0 1 .4 1 1 0 1.3.2 2.5.6 3.6.1.3 0 .7-.2 1z"/></svg>
        </li>
        <li class="contact-item">(555) 417-2863
          <svg viewBox="0 0 24 24"><path d="M7 1h10a2 2 0 0 1 2 2v18a2 2 0 0 1-2 2H7a2 2 0 0 1-2-2V3a2 2 0 0 1 2-2zm0 3v14h10V4zm5 15.5a1 1 0 1 0 0 2 1 1 0 0 0 0-2z"/></svg>
        </li>
        <li class="contact-item">(555) 301-4480
          <svg viewBox="0 0 24 24"><path d="M7 2h8v5H7zM4 8h16a2 2 0 0 1 2 2v10a2 2 0 0 1-2 2H4a2 2 0 0 1-2-2V10a2 2 0 0 1 2-2zm3 5v2h10v-2zm0 4v2h6v-2z"/></svg>
        </li>
        <li class="contact-item gap-above">mhale@whitcombe.example
          <svg viewBox="0 0 24 24"><path d="M2 5h20v14H2zm2 2v.5l8 5 8-5V7zm0 3v7h16v-7l-8 5z"/></svg>
        </li>
        <li class="contact-item">www.whitcombe.example
          <svg viewBox="0 0 24 24"><path d="M12 2a10 10 0 1 0 0 20 10 10 0 0 0 0-20zm6.9 9h-3a15 15 0 0 0-1.3-5.6A8 8 0 0 1 18.9 11zM12 4c.9 1.2 1.7 3.6 1.9 7h-3.8c.2-3.4 1-5.8 1.9-7zM9.4 5.4A15 15 0 0 0 8.1 11h-3a8 8 0 0 1 4.3-5.6zM5.1 13h3a15 15 0 0 0 1.3 5.6A8 8 0 0 1 5.1 13zM12 20c-.9-1.2-1.7-3.6-1.9-7h3.8c-.2 3.4-1 5.8-1.9 7zm2.6-1.4a15 15 0 0 0 1.3-5.6h3a8 8 0 0 1-4.3 5.6z"/></svg>
        </li>
      </ul>
    </section>
  </article>
</main>
</body>
</html>
```